TWS Business Card Design

As a full service media and advocacy firm, we lean on years of experience in political and corporate consulting, grassroots campaigning, media placement, and video production to deliver unparalleled results. Recently we have moved into digital media and now provide this service for our clients.

I will add our two company logos to be used on the business cards. The longer logo with "sky reach studio" is our primary logo. Our secondary logo is more square one with "sky reach" and 'digital.media.campaigns" on it. We are looking for clean and modern looking business cards fitting for a digital firm.

I will also add our logos that go well with dark backgrounds.

Industry/Entity Type

Political

Contact Information for Business Card

Denton Pratchard, Director of Campaigns and Digital, 571-482-7165, denton@skyreachstudioco.com, @SkyReachStudioCo, @DentonPratchard, Facebook.com/SkyReachStudioCo

```html
<!DOCTYPE html>
<html lang="en">
<head>
<meta charset="utf-8">
<title>Sky Reach Studio Business Card</title>
<link href="https://fonts.googleapis.com/css2?family=Montserrat:wght@400;500;600;700&display=swap" rel="stylesheet">
<style>
  :root {
    --backdrop: #2a2a2c;
    --brand-navy: #0d3c8c;
    --brand-navy-deep: #0a2f70;
    --brand-sky: #1a8ad6;
    --ink-dark: #1d2f5e;
    --card-white: #f7f7f8;
    --line-navy: #213a7a;
    --white: #ffffff;
  }
  * { box-sizing: border-box; margin: 0; padding: 0; }
  html, body {
    width: 1200px; height: 900px; overflow: hidden;
    background: var(--backdrop);
    font-family: "Montserrat", sans-serif;
  }
  .canvas { position: relative; width: 1200px; height: 900px; }
  .card {
    position: absolute; left: 320px; width: 560px; height: 320px;
    border-radius: 22px; overflow: hidden;
  }
  .card-front {
    top: 90px;
    background: linear-gradient(135deg, var(--brand-navy) 0%, var(--brand-navy-deep) 100%);
    display: flex; align-items: center; justify-content: center;
  }
  .front-wordmark {
    color: var(--white); font-weight: 600; font-size: 46px;
    letter-spacing: 1px; text-transform: uppercase;
  }
  .card-back {
    top: 490px; background: var(--card-white);
  }
  .back-logo {
    position: absolute; right: 40px; top: 34px; text-align: right;
  }
  .back-logo-name {
    color: var(--brand-sky); font-weight: 700; font-size: 38px;
    text-transform: uppercase; letter-spacing: 0.5px; line-height: 1;
  }
  .back-logo-rule {
    margin-top: 8px; height: 2px; width: 230px; background: var(--line-navy); margin-left: auto;
  }
  .divider {
    position: absolute; left: 255px; right: 40px; top: 150px;
    height: 1.5px; background: var(--line-navy);
  }
  .person { position: absolute; left: 34px; top: 170px; }
  .person-name {
    color: var(--brand-sky); font-weight: 700; font-size: 17px;
    text-transform: uppercase; letter-spacing: 0.3px;
  }
  .person-title { color: var(--ink-dark); font-size: 16px; margin-top: 2px; }
  .contact-list { list-style: none; margin-top: 18px; }
  .contact-list li, .social-list li {
    display: flex; align-items: center; gap: 9px;
    color: var(--ink-dark); font-size: 16px; line-height: 26px;
  }
  .icon {
    width: 17px; height: 17px; border-radius: 50%;
    background: var(--brand-sky); flex: none;
    display: flex; align-items: center; justify-content: center;
  }
  .social-list { list-style: none; position: absolute; right: 40px; top: 168px; }
</style>
</head>
<body>
<main class="canvas">
  <section class="card card-front" aria-label="Card front">
    <span class="front-wordmark">sky reach studio</span>
  </section>

  <section class="card card-back" aria-label="Card back">
    <div class="back-logo">
      <div class="back-logo-name">sky reach</div>
      <div class="back-logo-rule"></div>
    </div>

    <div class="divider"></div>

    <div class="person">
      <p class="person-name">Denton Pratchard</p>
      <p class="person-title">Director of Campaigns and Digital</p>
      <ul class="contact-list">
        <li>
          <span class="icon">
            <svg width="9" height="11" viewBox="0 0 9 11"><rect x="1" y="0.5" width="7" height="10" rx="1.5" fill="none" stroke="#fff" stroke-width="1.2"/><circle cx="4.5" cy="8.3" r="0.8" fill="#fff"/></svg>
          </span>571-482-7165
        </li>
        <li>
          <span class="icon">
            <svg width="11" height="8" viewBox="0 0 11 8"><rect x="0.5" y="0.5" width="10" height="7" rx="1" fill="none" stroke="#fff" stroke-width="1"/><path d="M0.8 1 L5.5 4.6 L10.2 1" fill="none" stroke="#fff" stroke-width="1"/></svg>
          </span>denton@skyreachstudioco.com
        </li>
        <li>
          <span class="icon">
            <svg width="11" height="11" viewBox="0 0 11 11"><circle cx="5.5" cy="5.5" r="4.8" fill="none" stroke="#fff" stroke-width="1"/><ellipse cx="5.5" cy="5.5" rx="2" ry="4.8" fill="none" stroke="#fff" stroke-width="0.9"/><path d="M0.7 5.5 H10.3" stroke="#fff" stroke-width="0.9"/></svg>
          </span>www.skyreachstudioco.com
        </li>
      </ul>
    </div>

    <ul class="social-list">
      <li><span class="icon"></span>@SkyReachStudioCo</li>
      <li><span class="icon"></span>@DentonPratchard</li>
      <li><span class="icon"></span>/SkyReachStudioCo</li>
    </ul>
  </section>
</main>
</body>
</html>
```